Business Card Design for Telecommunications and IT Solutions company "OKRA"

BC for telecommunications company name "OKRA" with slogan "Telecom & IT Solutions"

should have the full name as above "OKRA" and the slogan
color reqiured black, red (dark) and white

simple, professional, serious, modern design is required

1 side of business card have a full details, contacts and logo
other side have only the logo, website and full company name "ALOKRA Company for Telecommunications service & Information Technology LLC"

i have attached the logo and current business card sample and note that the logo was changed not the same in the attached business card

Industry/Entity Type

Telecommunications

Contact Information for Business Card

Full name: Omar Nabil Al Hudari
Job title: General Manager
Mobile no: +964xxxxxxxxx
email: omar@okra-tel.example
full name of the company: ALOKRA Company Telecommunications Services & Information Technology LLC.
website: www.okra-tel.example
address: Nakheel Dist. 148/7 JubailaQadim, Basra, Iraq

Requirements
Must have
• two languages in the same side of business card (English, Arabic) for only the name and title

```html
<!DOCTYPE html>
<html lang="en">
<head>
<meta charset="utf-8">
<title>OKRA Business Card</title>
<link rel="stylesheet" href="https://fonts.googleapis.com/css2?family=Cairo:wght@600;700&family=Roboto+Condensed:wght@700&family=Roboto:wght@500;700&family=Tinos:ital@0;1&display=swap">
<style>
  :root {
    --stage: #1c1c1c;
    --paper: #ffffff;
    --paper-shade: #e6e6e6;
    --red: #b3111b;
    --red-soft: #d8454e;
    --grey: #5a5a5a;
    --ink: #111111;
    --muted: #555555;
  }
  html, body {
    margin: 0;
    width: 1200px;
    height: 871px;
    overflow: hidden;
    background: var(--stage);
  }
  .stage {
    position: relative;
    width: 1200px;
    height: 871px;
  }
  .card {
    position: absolute;
    left: 260px;
    width: 680px;
    height: 389px;
    background: radial-gradient(ellipse at 60% 30%, var(--paper) 45%, var(--paper-shade) 100%);
    overflow: hidden;
    box-shadow: 0 10px 30px rgba(0,0,0,.5);
  }
  .card--company { top: 26px; }
  .card--contact { top: 456px; }

  .brand {
    display: flex;
    align-items: center;
    gap: 10px;
    font-family: "Roboto Condensed", sans-serif;
    font-weight: 700;
    color: var(--red);
  }
  .brand__dot {
    width: 22px; height: 22px;
    border-radius: 50%;
    background: var(--red);
  }
  .slogan {
    font-family: "Tinos", serif;
    color: var(--muted);
  }

  /* Company side */
  .company {
    position: absolute;
    inset: 0 0 60px 0;
    display: flex;
    flex-direction: column;
    align-items: center;
    padding-top: 34px;
    text-align: center;
  }
  .company .brand { font-size: 62px; line-height: 1; }
  .company .slogan { font-size: 15px; margin-top: 4px; }
  .company__name {
    margin-top: 16px;
    font-family: "Roboto", sans-serif;
    font-weight: 700;
    font-size: 20px;
    letter-spacing: 9px;
    color: var(--grey);
  }
  .company__name .accent { color: var(--red); }
  .company__line {
    font-family: "Roboto", sans-serif;
    font-weight: 700;
    font-size: 15px;
    color: var(--grey);
    margin-top: 4px;
  }
  .company__arabic {
    font-family: "Cairo", sans-serif;
    font-weight: 600;
    font-size: 19px;
    color: var(--grey);
    line-height: 1.35;
    margin-top: 6px;
  }
  .company__arabic .accent { color: var(--red); }
  .company__web {
    font-family: "Roboto", sans-serif;
    font-weight: 700;
    font-size: 17px;
    letter-spacing: 2px;
    color: var(--red);
    margin-top: 4px;
  }
  .company-band {
    position: absolute;
    left: 0; right: 0; bottom: 0;
    height: 26px;
    background: linear-gradient(90deg, var(--red-soft), var(--red));
  }

  /* Contact side */
  .contact-brand {
    position: absolute;
    left: 48px; top: 120px;
    width: 230px;
    display: flex;
    flex-direction: column;
    align-items: center;
  }
  .contact-brand .brand { font-size: 54px; line-height: 1; }
  .contact-brand .slogan { font-size: 14px; margin-top: 4px; }
  .divider {
    position: absolute;
    left: 318px; top: 40px;
    width: 2px; height: 250px;
    background: var(--red);
  }
  .details {
    position: absolute;
    left: 340px; top: 44px;
  }
  .person__name {
    font-family: "Roboto Condensed", sans-serif;
    font-weight: 700;
    font-size: 24px;
    color: var(--ink);
    letter-spacing: .5px;
  }
  .person__title {
    font-family: "Roboto", sans-serif;
    font-weight: 700;
    font-size: 15px;
    letter-spacing: 3px;
    color: var(--red);
    text-transform: uppercase;
  }
  .person__name-ar, .person__title-ar {
    font-family: "Cairo", sans-serif;
    font-weight: 700;
    line-height: 1.3;
  }
  .person__name-ar { font-size: 26px; color: var(--ink); margin-top: 4px; }
  .person__title-ar { font-size: 22px; color: var(--red); }
  .contacts {
    list-style: none;
    margin: 14px 0 0;
    padding: 0;
  }
  .contacts li {
    display: flex;
    align-items: center;
    gap: 14px;
    font-family: "Roboto Condensed", sans-serif;
    font-weight: 700;
    font-size: 21px;
    color: var(--ink);
    line-height: 1.5;
  }
  .contacts svg { width: 18px; height: 18px; flex: none; }

  .contact-bands {
    position: absolute;
    left: 0; right: 0; bottom: 0;
    height: 70px;
  }
  .contact-bands span { position: absolute; display: block; }
  .band-left { left: 0; width: 240px; top: 18px; height: 52px; background: linear-gradient(180deg, var(--red-soft), #c9666b); }
  .band-grey { left: 240px; width: 105px; top: 40px; height: 30px; background: var(--grey); }
  .band-black { left: 345px; width: 105px; top: 40px; height: 30px; background: var(--ink); }
  .band-right { left: 450px; right: 0; top: 40px; height: 30px; background: linear-gradient(90deg, var(--red), #7e0a11); }
</style>
</head>
<body>
<main class="stage">

  <section class="card card--company" aria-label="Company side">
    <div class="company">
      <div class="brand"><span class="brand__dot"></span>OKRA</div>
      <div class="slogan">Telecom &amp; IT Solutions</div>
      <div class="company__name"><span class="accent">A</span>LOKRA COMPANY</div>
      <div class="company__line">Telecommunications Services &amp; Information Technology LTD</div>
      <div class="company__arabic" dir="rtl">شركة <span class="accent">الأوكرا</span> خدمات الإتصالات<br>وتقنية المعلومات المحدودة</div>
      <div class="company__web">WWW.OKRA-TEL.EXAMPLE</div>
    </div>
    <div class="company-band"></div>
  </section>

  <section class="card card--contact" aria-label="Contact side">
    <div class="contact-brand">
      <div class="brand"><span class="brand__dot"></span>OKRA</div>
      <div class="slogan">Telecom &amp; IT Solutions</div>
    </div>
    <div class="divider"></div>
    <div class="details">
      <div class="person__name">Omar Nabil Al-Hudari</div>
      <div class="person__title">General Manager</div>
      <div class="person__name-ar" dir="rtl">عمر نبيل الحضري</div>
      <div class="person__title-ar" dir="rtl">المدير العام</div>
      <ul class="contacts">
        <li>
          <svg viewBox="0 0 18 18" aria-hidden="true"><rect x="5" y="1.5" width="8" height="15" rx="1.5" fill="none" stroke="#b3111b" stroke-width="1.6"/><line x1="8" y1="14" x2="10" y2="14" stroke="#b3111b" stroke-width="1.6"/></svg>
          +964 75550 120 36
        </li>
        <li>
          <svg viewBox="0 0 18 18" aria-hidden="true"><rect x="5" y="1.5" width="8" height="15" rx="1.5" fill="none" stroke="#b3111b" stroke-width="1.6"/><line x1="8" y1="14" x2="10" y2="14" stroke="#b3111b" stroke-width="1.6"/></svg>
          +964 75550 481 92
        </li>
        <li>
          <svg viewBox="0 0 18 18" aria-hidden="true"><rect x="1.5" y="4" width="15" height="10" fill="#b3111b"/><polyline points="1.5,4 9,10 16.5,4" fill="none" stroke="#fff" stroke-width="1.4"/></svg>
          omar@okra-tel.example
        </li>
      </ul>
    </div>
    <div class="contact-bands">
      <span class="band-left"></span>
      <span class="band-grey"></span>
      <span class="band-black"></span>
      <span class="band-right"></span>
    </div>
  </section>

</main>
</body>
</html>
```